Redesign of 2 real estate websites!

We need a redesign of our two real estate websites. These websites offer detailed information on the two real estates and need a modern fresh up.
Both websites should have the same design type, so you can see that they belong together, yet they should be in different colors. There is no logo to these pages, so the headlines can be integreated into the designs.
http://www.lindqvar-villa.de
http://www.osmund-lindqvar-haus.de/

```html
<!DOCTYPE html>
<html lang="de">
<head>
<meta charset="utf-8">
<title>Osmund-Lindqvar-Haus &amp; Lindqvar-Villa – Webdesign</title>
<link rel="stylesheet" href="https://fonts.googleapis.com/css2?family=Bebas+Neue&family=Exo+2:wght@400;500&display=swap">
<style>
  :root {
    --stage-grey: #e6e6e6;
    --stage-gap: #ffffff;
    --page-sand: #e3da98;
    --title-ink: #4b4b4b;
    --nav-blue: #168ac4;
    --nav-red: #c0242b;
    --menu-yellow: #f2e35a;
    --home-white: #ffffff;
    --shadow: rgba(0, 0, 0, 0.35);
  }
  * { margin: 0; padding: 0; box-sizing: border-box; }
  html, body {
    width: 1200px;
    height: 468px;
    overflow: hidden;
    background: var(--stage-gap);
  }
  .showcase {
    position: relative;
    width: 1200px;
    height: 468px;
  }
  .stage {
    position: absolute;
    top: 0;
    height: 468px;
    background: var(--stage-grey);
  }
  .stage--haus { left: 0; width: 590px; }
  .stage--villa { left: 610px; width: 590px; }

  .site {
    position: absolute;
    top: 0;
    width: 447px;
    height: 468px;
    background: var(--page-sand);
  }
  .stage--haus .site { left: 71px; }
  .stage--villa .site { left: 73px; }

  .site__title {
    position: absolute;
    top: 40px;
    left: 0;
    width: 100%;
    text-align: center;
    font-family: "Bebas Neue", sans-serif;
    font-weight: 400;
    font-size: 38px;
    letter-spacing: 0.5px;
    color: var(--title-ink);
  }

  .site__hero {
    position: absolute;
    top: 138px;
    left: 0;
    width: 447px;
    height: 236px;
    display: flex;
    box-shadow: 0 3px 6px var(--shadow);
  }
  .stage--villa .site__hero { top: 136px; height: 238px; }

  .nav {
    position: relative;
    z-index: 1;
    flex: none;
    height: 100%;
    padding-top: 10px;
    font-family: "Exo 2", sans-serif;
  }
  .nav--blue { width: 112px; background: var(--nav-blue); }
  .nav--red { width: 117px; background: var(--nav-red); }

  .nav__heading {
    text-align: center;
    font-size: 17px;
    font-weight: 400;
    color: var(--home-white);
    margin-bottom: 27px;
  }
  .nav__list {
    list-style: none;
    padding-left: 9px;
    padding-right: 4px;
  }
  .nav__item {
    font-size: 9.5px;
    line-height: 14.3px;
    letter-spacing: -0.2px;
    color: var(--menu-yellow);
    white-space: nowrap;
  }

  .photo {
    flex: 1;
    height: 100%;
  }
  .photo svg { display: block; width: 100%; height: 100%; }
</style>
</head>
<body>
<main class="showcase">

  <section class="stage stage--haus">
    <div class="site">
      <h1 class="site__title">Osmund - Lindqvar - Haus</h1>
      <div class="site__hero">
        <nav class="nav nav--blue">
          <h2 class="nav__heading">Home</h2>
          <ul class="nav__list">
            <li class="nav__item">Home</li>
            <li class="nav__item">Stadt Brenzfeld</li>
            <li class="nav__item">das Haus</li>
            <li class="nav__item">Wohnungen</li>
            <li class="nav__item">Wohnqualität</li>
            <li class="nav__item">Büros</li>
            <li class="nav__item">Klimaanlagen</li>
            <li class="nav__item">gewerbl. Mieter</li>
            <li class="nav__item">Links / Anfahrt</li>
          </ul>
        </nav>
        <div class="photo" role="img" aria-label="Foto: Marktplatz mit der bunten Häuserzeile des Osmund-Lindqvar-Hauses unter blauem Himmel">
          <svg viewBox="0 0 335 236" preserveAspectRatio="none">
            <defs>
              <linearGradient id="haus-scene" x1="0" y1="0" x2="0" y2="1">
                <stop offset="0" stop-color="#c9dcef"/>
                <stop offset="0.18" stop-color="#d8c3b8"/>
                <stop offset="0.45" stop-color="#e6cf96"/>
                <stop offset="0.72" stop-color="#b9a586"/>
                <stop offset="1" stop-color="#c2bdb6"/>
              </linearGradient>
            </defs>
            <rect width="335" height="236" fill="url(#haus-scene)"/>
          </svg>
        </div>
      </div>
    </div>
  </section>

  <section class="stage stage--villa">
    <div class="site">
      <h1 class="site__title">Die Lindqvar - Villa</h1>
      <div class="site__hero">
        <nav class="nav nav--red">
          <h2 class="nav__heading">Home</h2>
          <ul class="nav__list">
            <li class="nav__item">Home</li>
            <li class="nav__item">Stadt Brenzfeld</li>
            <li class="nav__item">Bauentwurf</li>
            <li class="nav__item">Eigentümer &amp; Bewohner</li>
            <li class="nav__item">die Villa</li>
            <li class="nav__item">Kontakt</li>
            <li class="nav__item">Links / Anfahrt</li>
            <li class="nav__item">Impressum</li>
            <li class="nav__item">Vermietung</li>
          </ul>
        </nav>
        <div class="photo" role="img" aria-label="Foto: rote Backsteinvilla hinter Bäumen mit parkenden Autos an der Straße">
          <svg viewBox="0 0 330 238" preserveAspectRatio="none">
            <defs>
              <linearGradient id="villa-scene" x1="0" y1="0" x2="1" y2="1">
                <stop offset="0" stop-color="#3f5a2c"/>
                <stop offset="0.35" stop-color="#6d7d52"/>
                <stop offset="0.6" stop-color="#b5655a"/>
                <stop offset="0.85" stop-color="#c9b7a6"/>
                <stop offset="1" stop-color="#d9d4cc"/>
              </linearGradient>
            </defs>
            <rect width="330" height="238" fill="url(#villa-scene)"/>
          </svg>
        </div>
      </div>
    </div>
  </section>

</main>
</body>
</html>
```